Building Servicess

We need a new business card design for a company. We specialise in: Electrical/Site temporary electrics, Data/Network Installation, Passive Fire Protection

Industry/Entity Type

Construction

Contact Information for Business Card

Services provided as detailed on project description

Font styles to use
Serif

Colors
0054AA
0677BA
7BADD7
CADEEF
E8F1F8
00AB8E
00BBA5
67D7C9
C6EFE9
E9F9F6
EB3D1F
EC4F4E
F09395
F8D3D4
FCEDEE

Requirements
Must have
• Company logo-contact details-phone numbers

```html
<!DOCTYPE html>
<html lang="en">
<head>
<meta charset="utf-8">
<title>Ridgeway Site Services – Business Card</title>
<link href="https://fonts.googleapis.com/css2?family=Old+Standard+TT:wght@400;700&display=swap" rel="stylesheet">
<style>
  :root {
    --brand-blue: #1077bc;
    --accent-blue: #4bb2ff;
    --ink-white: #ffffff;
    --card-edge: #dedede;
    --page-bg: #ffffff;
  }
  html, body {
    margin: 0;
    padding: 0;
    width: 1200px;
    height: 1200px;
    overflow: hidden;
    background: var(--page-bg);
  }
  .business-card {
    position: absolute;
    left: 183px;
    top: 363px;
    width: 841px;
    height: 481px;
    box-sizing: border-box;
    border: 1px solid var(--card-edge);
    background: var(--ink-white);
    overflow: hidden;
    font-family: "Old Standard TT", "Times New Roman", serif;
  }
  .card-artwork {
    position: absolute;
    inset: 0;
  }
  .holder-name {
    position: absolute;
    left: 68px;
    top: 72px;
    margin: 0;
    font-size: 44px;
    font-weight: 400;
    letter-spacing: 0.5px;
    color: var(--ink-white);
    line-height: 1;
  }
  .holder-role {
    position: absolute;
    left: 68px;
    top: 124px;
    margin: 0;
    font-size: 25px;
    color: var(--ink-white);
    line-height: 1;
  }
  .role-rule {
    position: absolute;
    left: 70px;
    top: 154px;
    width: 177px;
    height: 2px;
    background: var(--accent-blue);
  }
  .contact-list {
    position: absolute;
    left: 70px;
    top: 268px;
    margin: 0;
    padding: 0;
    list-style: none;
  }
  .contact-item {
    display: flex;
    align-items: center;
    height: 40px;
    font-size: 25px;
    color: var(--ink-white);
    letter-spacing: 0.3px;
  }
  .contact-icon {
    width: 20px;
    height: 20px;
    margin-right: 12px;
    flex: none;
  }
  .company-name {
    position: absolute;
    left: 480px;
    width: 300px;
    top: 82px;
    margin: 0;
    text-align: center;
    font-size: 34px;
    font-weight: 700;
    line-height: 1.15;
    color: var(--brand-blue);
    letter-spacing: 1px;
  }
</style>
</head>
<body>
  <article class="business-card">
    <svg class="card-artwork" width="841" height="481" viewBox="0 0 841 481" aria-hidden="true">
      <polygon class="panel-main" fill="var(--brand-blue)" points="0,0 351,0 562,363 631,481 0,481"/>
      <polygon class="panel-accent" fill="var(--accent-blue)" points="351,0 562,363 499,416"/>
    </svg>

    <h1 class="holder-name">FULL NAME</h1>
    <p class="holder-role">CEO &amp; Founder</p>
    <div class="role-rule"></div>

    <ul class="contact-list">
      <li class="contact-item">
        <svg class="contact-icon" viewBox="0 0 24 24" aria-hidden="true"><path fill="var(--accent-blue)" d="M6.6 2.5c.8-.4 1.6.2 1.8 1l.8 2.6c.2.7-.1 1.3-.6 1.7l-1 .7c.9 2.3 2.8 4.4 5.2 5.5l.8-.9c.5-.5 1.2-.7 1.8-.4l2.5 1c.8.3 1.2 1.2.8 1.9-.9 1.9-2.7 2.9-4.6 2.2C8.6 16.4 5 12.3 4.4 7.3c-.2-2 .7-3.9 2.2-4.8z"/></svg>
        <span>000 111 222 333</span>
      </li>
      <li class="contact-item">
        <svg class="contact-icon" viewBox="0 0 24 24" aria-hidden="true"><rect x="2" y="6" width="20" height="12" fill="none" stroke="var(--accent-blue)" stroke-width="1"/><path d="M2 6l10 8 10-8M2 18l7-6M22 18l-7-6" fill="none" stroke="var(--accent-blue)" stroke-width="1"/></svg>
        <span>yourgmail@name.com</span>
      </li>
      <li class="contact-item">
        <svg class="contact-icon" viewBox="0 0 24 24" aria-hidden="true"><g fill="none" stroke="var(--accent-blue)" stroke-width="1.2"><circle cx="12" cy="12" r="9.5"/><ellipse cx="12" cy="12" rx="4.5" ry="9.5"/><path d="M2.5 12h19M4 7h16M4 17h16M12 2.5v19"/></g></svg>
        <span>www.websitename.com</span>
      </li>
      <li class="contact-item">
        <svg class="contact-icon" viewBox="0 0 24 24" aria-hidden="true"><path fill="var(--accent-blue)" d="M12 2c3.6 0 6 2.6 6 6 0 4-6 14-6 14S6 12 6 8c0-3.4 2.4-6 6-6zm0 3.4a2.6 2.6 0 1 0 0 5.2 2.6 2.6 0 0 0 0-5.2z"/></svg>
        <span>Your Street Adress Here</span>
      </li>
    </ul>

    <p class="company-name">RIDGEWAY<br>SITE SERVICES LTD</p>
  </article>
</body>
</html>
```